Funk up our website

Our website is currently in operation and working well, see it at www.clearbriefhub.co.uk

However it needs some redesign work, to help it feel fresh, inviting and friendly.

We need graphic mockups (png hi-res) to pass to the dev team, to do the css work:

homepage - http://www.clearbriefhub.co.uk
topic page - http://www.clearbriefhub.co.uk/guidance/business
sub-topic - http://www.clearbriefhub.co.uk/guidance/business/goods-services
content - http://www.clearbriefhub.co.uk/guidance/business/goods-services/heads-of-terms
ancillary pages - contact us, heads of terms, etc

The structure of the page in terms of the placement of header, menu bar, content area and footer needs to remain, but the design of it is up for grabs.

The site is currently free to use, but in the future will have the aim of getting users to register for free, but with the option of buying documents on an individual basis, or subscription basis, or subscribing to additional legal services.

Additional information
---------------------------
Users
1. Owners and managers in small and medium businesses
2. In the UK only
3. Who find dealing with legal issues and lawyers intimidating
4. Who are searching for online help to try and avoid having to deal with a lawyer
5. Or have been referred via social media
Desired user experience
1. A welcoming, friendly site
2. That takes the complexity out of dealing with legal issues
3. That really does clear the brief
4. That is fast, efficient and clear
5. That is pleasantly different from the normal experience of interacting with a law firm
Relevant factors
1. Most visitors will first land on a content page (e.g. [link]) via a search result or banner advertisement – not the Home Page
2. Repeat visitors are more likely to go to the Home Page
3. Works with web responsive design techniques for display on smartphones and tablets
4. Implemented through CSS
Colour palette
Designer should feel able to build the palette around the following core colours
CMYK
YELLOW = 0,25,100,0
GREEN = 80,0,100,0
BLUE = 100,25,0,0

RGB
YELLOW = 255,195,15
GREEN = 15,175,75
BLUE = 0,140,210

PANTONE
YELLOW = 123c
GREEN = 361c
BLUE = 3005c

Fonts
Soho Gothic, Soho, Arial
Designer should feel able to add fonts to complement these core fonts.

Our logo needs to remain (see attached document) Our strap line, can be changed if needed.

Best
RK
Updates

Hi All

Some websites worth having a look at for how people have done things differently / added something distinctive to their website:

http://www.brevicounsel.co.uk/
https://www.tandelegal.co.uk/
http://www.quillatrix.com/

Cheers
RK

Hi All

Thanks for your designs. Just back in the office today, we will discuss and feedback / decide asap.

Best
RK

```html
<!DOCTYPE html>
<html lang="en">
<head>
<meta charset="utf-8">
<title>Trade &amp; e-commerce – Clear Brief Hub</title>
<link href="https://fonts.googleapis.com/css2?family=Arimo:wght@400;700&display=swap" rel="stylesheet">
<style>
  :root {
    --yellow: #ffc30f;
    --green: #0faf4b;
    --blue: #008cd2;
    --blue-light: #1aa3e6;
    --orange: #ffa800;
    --grey-btn: #bfbfbf;
    --text: #444444;
    --text-soft: #555555;
    --crumb-bg: #f1f2f4;
    --side-social: #3b5b98;
    --side-short: #2aa9e0;
    --side-mail: #7a8c90;
    --side-print: #6c8185;
    --side-more: #ff6d4f;
  }
  * { box-sizing: border-box; margin: 0; padding: 0; }
  html, body { width: 1200px; height: 720px; overflow: hidden; }
  body {
    position: relative;
    font-family: "Arimo", Arial, sans-serif;
    color: var(--text);
    background: linear-gradient(#f8f8f8 145px, #ececec 610px);
  }
  .site-header {
    position: absolute; left: 0; top: 0; width: 1200px; height: 113px;
    background: #ffffff; border-bottom: 1px solid #e4e4e4;
  }
  .brand {
    position: absolute; left: 103px; top: 30px;
    display: flex; align-items: center; gap: 12px;
    font-size: 34px; font-weight: 700; color: #111111; letter-spacing: -0.5px;
  }
  .brand-mark { width: 44px; height: 44px; background: var(--green); }
  .search {
    position: absolute; left: 642px; top: 19px; width: 236px; height: 27px;
    border: 1px solid #c8c8c8; border-radius: 14px; overflow: hidden; background: #fff;
    display: flex;
  }
  .search-field { flex: 1; display: flex; align-items: center; padding-left: 12px; gap: 6px; font-size: 14px; color: #8a8a8a; }
  .search-btn {
    width: 64px; background: var(--orange); color: #fff; font-size: 11px; font-weight: 700;
    display: flex; align-items: center; justify-content: center;
  }
  .account-links { position: absolute; left: 890px; top: 28px; font-size: 10px; color: #444; letter-spacing: .3px; }
  .account-links .sep { color: var(--blue); margin: 0 6px; }
  .social-dots { position: absolute; left: 1010px; top: 20px; display: flex; gap: 8px; }
  .social-dots span { width: 24px; height: 24px; border-radius: 50%; }
  .main-nav { position: absolute; left: 483px; top: 64px; display: flex; gap: 2px; }
  .main-nav a {
    height: 34px; border-radius: 6px; background: var(--grey-btn); color: #fff;
    font-size: 12px; display: flex; align-items: center; justify-content: center;
    text-decoration: none; letter-spacing: .2px;
  }
  .main-nav a.active { background: var(--green); }
  .breadcrumb {
    position: absolute; left: 0; top: 114px; width: 1200px; height: 31px;
    background: var(--crumb-bg); font-size: 11px; color: #555; padding: 9px 0 0 110px;
  }
  .breadcrumb .current { color: var(--green); }
  .page-title { position: absolute; left: 112px; top: 168px; font-size: 24px; font-weight: 400; color: #111; }
  .area-bar {
    position: absolute; left: 112px; top: 201px; width: 976px; height: 36px;
    border-radius: 8px 8px 0 0; background: linear-gradient(var(--blue-light), var(--blue));
    color: #fff; font-size: 16px; font-weight: 700; padding: 9px 0 0 24px;
  }
  .topic { position: absolute; width: 400px; padding-left: 15px; }
  .topic::before {
    content: ""; position: absolute; left: 0; top: 2px;
    border-left: 5px solid var(--green); border-top: 5px solid transparent; border-bottom: 5px solid transparent;
  }
  .topic h3 { font-size: 13px; font-weight: 700; color: var(--text); line-height: 15px; }
  .topic p { font-size: 12px; color: var(--text-soft); line-height: 15px; }
  .share-bar { position: absolute; left: 0; top: 202px; width: 48px; }
  .share-bar div { height: 49px; display: flex; align-items: center; justify-content: center; }
  .feedback-tab {
    position: absolute; left: 1168px; top: 360px; width: 32px; height: 100px;
    border: 2px solid var(--green); background: #fff;
    display: flex; align-items: center; justify-content: center;
  }
  .feedback-tab span { transform: rotate(-90deg); color: var(--green); font-size: 17px; font-weight: 700; }
  .footer-band { position: absolute; left: 0; top: 614px; width: 1200px; height: 14px; background: var(--yellow); }
  .footer-links {
    position: absolute; left: 0; top: 628px; width: 1200px; height: 62px; background: #fff;
    display: flex; justify-content: center; align-items: center; font-size: 11.5px; color: #333; letter-spacing: .2px;
  }
  .footer-links .sep { color: var(--green); margin: 0 12px; }
  .copyright {
    position: absolute; left: 0; top: 690px; width: 1200px; height: 30px; background: var(--yellow);
    color: #fff; font-size: 11px; padding: 10px 0 0 112px;
  }
</style>
</head>
<body>
  <header class="site-header">
    <div class="brand"><span class="brand-mark"></span>Clear Brief Hub</div>
    <div class="search">
      <div class="search-field">
        <svg width="14" height="14" viewBox="0 0 14 14"><circle cx="6" cy="6" r="4.5" fill="#cfe7f5" stroke="#6a8da0" stroke-width="1.4"/><line x1="9.3" y1="9.3" x2="13" y2="13" stroke="#6a8da0" stroke-width="2"/></svg>
        Search
      </div>
      <div class="search-btn">SEARCH</div>
    </div>
    <div class="account-links">REGISTER<span class="sep">|</span>LOGIN</div>
    <div class="social-dots">
      <span style="background:#3b5998"></span>
      <span style="background:#2aa9e0"></span>
      <span style="background:#3d8bc9"></span>
    </div>
    <nav class="main-nav">
      <a href="#" style="width:75px">HOME</a>
      <a href="#" class="active" style="width:126px">GUIDE YOURSELF</a>
      <a href="#" style="width:126px">DRAFT YOURSELF</a>
      <a href="#" style="width:156px">SEARCH FOR A LAWYER</a>
      <a href="#" style="width:126px">GET YOUR DRAFTS</a>
    </nav>
  </header>

  <div class="breadcrumb">Home &gt;&nbsp; Guide Yourself &gt;&nbsp; Business &gt;&nbsp; <span class="current">Trade &amp; e-commerce</span></div>

  <h1 class="page-title">Trade &amp; e-commerce</h1>
  <div class="area-bar">First, choose the area</div>

  <div class="topic" style="left:136px;top:269px"><h3>Buy and sell goods and services</h3><p>Deal with the terms, conditions and contracts under which you negotiate, buy and sell</p></div>
  <div class="topic" style="left:136px;top:327px"><h3>Sell products and services through distributors</h3><p>Appoint and manage distributors to grow your business</p></div>
  <div class="topic" style="left:136px;top:372px"><h3>Protect your intellectual property and business information</h3><p>What do you need to do to protect and benefit from the information and intellectual property assets that your business has?</p></div>
  <div class="topic" style="left:136px;top:430px"><h3>Outsource</h3><p>Assess whether outsourcing is a viable option for your business</p></div>
  <div class="topic" style="left:136px;top:474px"><h3>Protect data and privacy</h3><p>Ensure your business complies with the rules and regulations on data protection and the privacy of people with whom you deal</p></div>

  <div class="topic" style="left:597px;top:269px"><h3>Deal with consumers</h3><p>Understand how you can and cannot trade with consumers</p></div>
  <div class="topic" style="left:597px;top:327px"><h3>Sell products and services through commercial agents</h3><p>Grow your business by appointing agents to sell for you</p></div>
  <div class="topic" style="left:597px;top:372px"><h3>Deal with IT and e-commerce</h3><p>Manage the development, sales, procurement and use of IT, websites and software</p></div>
  <div class="topic" style="left:597px;top:430px"><h3>Understand rules on bribery</h3><p>What must you do to comply with the Bribery Act 2010?</p></div>
  <div class="topic" style="left:597px;top:474px"><h3>Franchise a business</h3><p>Franchise a business or buy a franchise</p></div>

  <aside class="share-bar">
    <div style="background:var(--side-social)"></div>
    <div style="background:var(--side-short)"></div>
    <div style="background:var(--side-mail)">
      <svg width="22" height="15" viewBox="0 0 22 15"><rect x="1" y="1" width="20" height="13" fill="none" stroke="#fff" stroke-width="2"/><polyline points="1,1 11,9 21,1" fill="none" stroke="#fff" stroke-width="2"/></svg>
    </div>
    <div style="background:var(--side-print)">
      <svg width="20" height="18" viewBox="0 0 20 18"><rect x="5" y="0" width="10" height="5" fill="#fff"/><rect x="0" y="5" width="20" height="8" rx="1" fill="#fff"/><rect x="5" y="10" width="10" height="8" fill="#fff" stroke="#6c8185" stroke-width="1.5"/></svg>
    </div>
    <div style="background:var(--side-more)">
      <svg width="18" height="18" viewBox="0 0 18 18"><rect x="7" y="0" width="4" height="18" fill="#fff"/><rect x="0" y="7" width="18" height="4" fill="#fff"/></svg>
    </div>
  </aside>

  <div class="feedback-tab"><span>feedback</span></div>

  <div class="footer-band"></div>
  <footer class="footer-links">
    CONTACT US<span class="sep">|</span>ABOUT US<span class="sep">|</span>TERMS AND CONDITIONS<span class="sep" style="color:#333">|</span>PRIVACY POLICY<span class="sep">|</span>TERMINATE USER ACCOUNT<span class="sep">|</span>FAQS FOR USERS<span class="sep">|</span>IF YOU'RE A LAWYER
  </footer>
  <div class="copyright">© Lucent Legal Limited 2012</div>
</body>
</html>
```